Professional business cards for real estate development company

I need business cards for my new real estate development company. The company, "KORVA" is a real estate development, investment, and advisory firm with a focus on multifamily, office, and mixed-use projects across primary and secondary markets in the Southeast United States.

Style preference is modern

Industry/Entity Type

Real Estate Development

Contact Information for Business Card

The business cards need to include:
Name
Title
Mailing Address
Phone Number
Web Address

Logo is attached. I would like white to be the primary color with incorporation of the company colors: #232D3A and #B5A451

Font styles to use
Other font styles liked:
• Montserrat, Avenir

Requirements
Must have
• Company Logo. No need to include the company name since the name is in the logo.
Should not have
• No line type designs

```html
<!DOCTYPE html>
<html lang="en">
<head>
<meta charset="utf-8">
<title>KORVA business cards</title>
<link href="https://fonts.googleapis.com/css2?family=Work+Sans:wght@400;600&display=swap" rel="stylesheet">
<style>
  :root {
    --navy: #232d3a;
    --navy-soft: #2e3b4d;
    --white: #ffffff;
    --ink: #1f2833;
    --grey: #4a4f57;
    --accent-grey: #8a8d92;
    --stage: #2a2a2a;
  }
  * { margin: 0; padding: 0; box-sizing: border-box; }
  html, body {
    width: 1152px; height: 1200px; overflow: hidden;
    background: var(--stage);
    font-family: "Work Sans", sans-serif;
  }
  .card {
    position: absolute; left: 226px;
    width: 700px; height: 400px;
    box-shadow: 0 10px 30px rgba(0,0,0,.5);
    overflow: hidden;
  }
  .card-front { top: 130px; background: var(--navy); }
  .card-back { top: 640px; background: var(--white); }

  .front-mark {
    position: absolute; left: 0; right: 0; top: 160px;
    display: flex; justify-content: center; align-items: center; gap: 18px;
    color: var(--navy-soft);
    font-weight: 600; font-size: 64px; letter-spacing: 4px;
  }
  .mark-square { width: 40px; height: 40px; background: var(--navy-soft); }

  .brand {
    position: absolute; left: 60px; top: 130px;
    display: flex; align-items: center; gap: 14px;
    color: var(--navy);
    font-weight: 600; font-size: 62px; letter-spacing: 3px;
  }
  .brand .mark-square { width: 34px; height: 34px; background: var(--navy); }

  .divider {
    position: absolute; left: 385px; top: 90px;
    width: 2px; height: 175px; background: var(--navy);
  }
  .contact {
    position: absolute; left: 415px; top: 95px;
    color: var(--grey); font-size: 17px; line-height: 1.35;
  }
  .contact-name {
    color: var(--ink); font-weight: 600; font-size: 25px; letter-spacing: 1.5px;
  }
  .contact-title { margin-bottom: 14px; }
  .contact-address { margin-bottom: 8px; }
  .contact-line { display: flex; align-items: center; gap: 8px; }
  .contact-line svg { width: 13px; height: 13px; flex: none; }

  .footer-band { position: absolute; left: 0; bottom: 0; width: 700px; height: 90px; }
</style>
</head>
<body>

<section class="card card-front">
  <div class="front-mark"><span class="mark-square"></span>KORVA</div>
</section>

<section class="card card-back">
  <div class="brand"><span class="mark-square"></span>KORVA</div>

  <div class="divider"></div>

  <div class="contact">
    <div class="contact-name">DANIEL HARLOW</div>
    <div class="contact-title">Director</div>
    <div class="contact-address">402 Alder Row<br>Marion, GA 30412</div>
    <div class="contact-line">
      <svg viewBox="0 0 16 16"><path d="M4 1l3 3-2 2c1 2 3 4 5 5l2-2 3 3-2 3C7 15 1 9 1 3z" fill="var(--grey)"/></svg>
      +1 555 201 4478
    </div>
    <div class="contact-line">
      <svg viewBox="0 0 16 16"><rect x="1" y="3" width="14" height="10" fill="none" stroke="var(--grey)" stroke-width="1.5"/><path d="M1 3l7 6 7-6" fill="none" stroke="var(--grey)" stroke-width="1.5"/></svg>
      hello@korvadev.com
    </div>
    <div class="contact-line">
      <svg viewBox="0 0 16 16"><circle cx="8" cy="8" r="6.5" fill="none" stroke="var(--grey)" stroke-width="1.3"/><ellipse cx="8" cy="8" rx="3" ry="6.5" fill="none" stroke="var(--grey)" stroke-width="1.1"/><path d="M1.5 8h13" stroke="var(--grey)" stroke-width="1.1"/></svg>
      korvadevelopment.com
    </div>
  </div>

  <svg class="footer-band" viewBox="0 0 700 90" preserveAspectRatio="none">
    <path d="M180 90 C 300 64, 480 58, 650 66 C 480 62, 300 70, 200 90 Z" fill="var(--accent-grey)"/>
    <path d="M205 90 C 330 74, 520 68, 700 46 L 700 90 Z" fill="var(--navy)"/>
  </svg>
</section>

</body>
</html>
```